Zentrix Banner Grid Ads for Custom Software Company

We need some images for display on the Zentrix Banner Grid. Need a collection of them at different sizes.

This is for a custom software development company that specializes in small to medium size businesses.

PLEASE PLEASE PLEASE GET CREATIVE! That is the point! Something very typical and plain will not win!

Target Market(s)

Small and Medium sized businesses looking for custom software development services

Industry/Entity Type

Computer Software

Font styles to use
Serif
Sans Serif

Requirements
Must have
• Medium Rectangle (300×250)
• Large Rectangle (336×280)
• Leaderboard (728×90)
• Half Page (300×600)
• Large Mobile Banner (320×100)
• Needs to stand out, but not be obnoxious
• Needs to flow with the website design and colors (does not need to be the same colors, just needs to work together)
• Must have specific call to action (schedule appointment or read more are options, but feel free to make up more)
Nice to have
• Logo integration
• Adobe Illustrator files with artboards/exports for the different sizes
Should not have
• Should not have more than 20% text
• Don't steal from the slides on the website. We want "read more" to mean read more, not more of the same.

```html
<!DOCTYPE html>
<html lang="en">
<head>
<meta charset="utf-8">
<title>Zentrix Banner Grid – Novalith display set</title>
<link href="https://fonts.googleapis.com/css2?family=Lato:wght@400&family=Montserrat:wght@400;500;700&display=swap" rel="stylesheet">
<style>
  :root {
    --board: #3d3d3d;
    --label: #ffffff;
    --brand-blue: #0a96d8;
    --brand-blue-light: #22a8e6;
    --cta-yellow: #fdc110;
    --cta-text: #1b1b1b;
    --ink-white: #ffffff;
    --art-light: #f4f4f4;
    --art-mid: #c4c4c4;
    --art-dark: #5a5a5a;
  }
  * { box-sizing: border-box; margin: 0; padding: 0; }
  html, body { width: 1200px; height: 1200px; overflow: hidden; background: var(--board); }
  .board { position: relative; width: 1200px; height: 1200px; font-family: "Montserrat", sans-serif; }

  .size-label {
    position: absolute; font-family: "Lato", sans-serif; font-size: 21px;
    color: var(--label); line-height: 1;
  }

  .banner { position: absolute; overflow: hidden; background: var(--brand-blue); }
  .banner-art {
    position: absolute; inset: 0;
    background: linear-gradient(160deg, var(--art-light) 0%, var(--art-mid) 55%, var(--art-dark) 100%);
  }
  .banner-shape { position: absolute; inset: 0; width: 100%; height: 100%; }
  .megaphone { position: absolute; }

  .copy { position: absolute; color: var(--ink-white); text-align: center; white-space: nowrap; }
  .brand { display: inline-flex; align-items: center; font-weight: 400; line-height: 1; }
  .brand-square { display: inline-block; background: var(--ink-white); margin-right: 0.25em; }
  .tagline-top { font-weight: 500; letter-spacing: 0.06em; line-height: 1; }
  .tagline-main { font-weight: 700; letter-spacing: 0.05em; line-height: 1; }
  .cta {
    display: inline-flex; align-items: center; justify-content: center;
    background: var(--cta-yellow); color: var(--cta-text); font-weight: 700;
    border-radius: 0.6em; box-shadow: 0 2px 0 rgba(0,0,0,0.18); letter-spacing: -0.02em;
  }

  /* 300 x 250 */
  .medium-rect { left: 170px; top: 104px; width: 327px; height: 272px; }
  .medium-rect .copy { left: 146px; top: 156px; width: 160px; }
  .medium-rect .brand { font-size: 19px; }
  .medium-rect .brand-square { width: 15px; height: 15px; }
  .medium-rect .tagline-top { font-size: 10.5px; margin-top: 14px; }
  .medium-rect .tagline-main { font-size: 16px; margin-top: 5px; }
  .medium-rect .cta { font-size: 8px; width: 64px; height: 21px; margin-top: 6px; }
  .medium-rect .megaphone { left: 28px; top: 184px; width: 62px; height: 70px; }

  /* 336 x 280 */
  .large-rect { left: 170px; top: 439px; width: 366px; height: 305px; }
  .large-rect .copy { left: 169px; top: 172px; width: 180px; }
  .large-rect .brand { font-size: 20px; }
  .large-rect .brand-square { width: 16px; height: 16px; }
  .large-rect .tagline-top { font-size: 11.5px; margin-top: 15px; }
  .large-rect .tagline-main { font-size: 18px; margin-top: 6px; }
  .large-rect .cta { font-size: 9.5px; width: 78px; height: 25px; margin-top: 12px; }
  .large-rect .megaphone { left: 34px; top: 212px; width: 70px; height: 78px; }

  /* 300 x 600 */
  .half-page { left: 710px; top: 104px; width: 327px; height: 654px; }
  .half-page .copy { left: 0; top: 432px; width: 327px; }
  .half-page .brand { font-size: 30px; }
  .half-page .brand-square { width: 24px; height: 24px; }
  .half-page .tagline-top { font-size: 21px; margin-top: 30px; }
  .half-page .tagline-main { font-size: 29px; margin-top: 10px; }
  .half-page .cta { font-size: 17px; width: 136px; height: 47px; margin-top: 20px; border-radius: 14px; }
  .half-page .megaphone { left: 88px; top: 312px; width: 100px; height: 112px; }

  /* 320 x 100 */
  .mobile-banner { left: 170px; top: 818px; width: 350px; height: 109px; }
  .mobile-banner .copy { left: 17px; top: 10px; text-align: left; }
  .mobile-banner .tagline-top { font-size: 9.5px; }
  .mobile-banner .tagline-main { font-size: 15px; margin-top: 6px; }
  .mobile-banner .brand { font-size: 14px; margin-top: 6px; }
  .mobile-banner .brand-square { width: 12px; height: 12px; }
  .mobile-banner .cta { font-size: 6.5px; width: 52px; height: 17px; margin-top: 8px; border-radius: 6px; }
  .mobile-banner .megaphone { left: 112px; top: 38px; width: 66px; height: 66px; }
  .mobile-banner .banner-art { left: auto; width: 190px; }

  /* 728 x 90 */
  .leaderboard { left: 170px; top: 1001px; width: 870px; height: 108px; }
  .leaderboard .copy { left: 29px; top: 14px; text-align: left; }
  .leaderboard .tagline-main { font-size: 15px; letter-spacing: 0.04em; }
  .leaderboard .cta-row { display: flex; align-items: center; margin-top: 17px; }
  .leaderboard .cta { font-size: 13px; width: 99px; height: 34px; border-radius: 10px; }
  .leaderboard .brand { font-size: 22px; margin-left: 31px; }
  .leaderboard .brand-square { width: 18px; height: 18px; }
  .leaderboard .megaphone { left: 300px; top: 18px; width: 80px; height: 86px; }
  .leaderboard .banner-art { left: auto; width: 490px; }
</style>
</head>
<body>
<svg width="0" height="0" style="position:absolute" aria-hidden="true">
  <defs>
    <symbol id="icon-megaphone" viewBox="0 0 80 100">
      <path d="M14 58 L50 10 L74 44 L24 74 Z" fill="#ffffff"/>
      <ellipse cx="62" cy="27" rx="10" ry="22" transform="rotate(-35 62 27)" fill="#ffffff" stroke="#0a96d8" stroke-width="3"/>
      <circle cx="15" cy="66" r="9" fill="#ffffff" stroke="#0a96d8" stroke-width="3"/>
      <path d="M28 70 L40 96 L50 91 L40 66 Z" fill="#ffffff" stroke="#0a96d8" stroke-width="2"/>
    </symbol>
    <radialGradient id="blue-glow" cx="30%" cy="80%" r="90%">
      <stop offset="0" stop-color="#22a8e6"/>
      <stop offset="1" stop-color="#0a96d8"/>
    </radialGradient>
  </defs>
</svg>

<main class="board">
  <!-- Medium rectangle -->
  <div class="size-label" style="left:169px;top:66px">300_250</div>
  <section class="banner medium-rect">
    <div class="banner-art" role="img" aria-label="Grayscale illustration of hands typing on a laptop among bar charts, gears and a euro coin"></div>
    <svg class="banner-shape" viewBox="0 0 327 272" preserveAspectRatio="none" aria-hidden="true">
      <polygon points="0,40 92,200 327,86 327,272 0,272" fill="url(#blue-glow)"/>
    </svg>
    <svg class="megaphone" aria-hidden="true"><use href="#icon-megaphone"/></svg>
    <div class="copy">
      <div class="brand"><span class="brand-square"></span>Novalith</div>
      <div class="tagline-top">A COMPLETE RANGE</div>
      <div class="tagline-main">OF SOFTWARE</div>
      <a class="cta">READ MORE</a>
    </div>
  </section>

  <!-- Large rectangle -->
  <div class="size-label" style="left:169px;top:410px">336_280</div>
  <section class="banner large-rect">
    <div class="banner-art" role="img" aria-label="Grayscale illustration of hands typing on a laptop among bar charts, gears and a clipboard"></div>
    <svg class="banner-shape" viewBox="0 0 366 305" preserveAspectRatio="none" aria-hidden="true">
      <polygon points="0,89 92,216 366,87 366,305 0,305" fill="url(#blue-glow)"/>
    </svg>
    <svg class="megaphone" aria-hidden="true"><use href="#icon-megaphone"/></svg>
    <div class="copy">
      <div class="brand"><span class="brand-square"></span>Novalith</div>
      <div class="tagline-top">A COMPLETE RANGE</div>
      <div class="tagline-main">OF SOFTWARE</div>
      <a class="cta">READ MORE</a>
    </div>
  </section>

  <!-- Mobile banner -->
  <div class="size-label" style="left:169px;top:786px">320_100</div>
  <section class="banner mobile-banner">
    <div class="banner-art" style="right:0" role="img" aria-label="Grayscale illustration of hands typing on a laptop beside bar charts"></div>
    <svg class="banner-shape" viewBox="0 0 350 109" preserveAspectRatio="none" aria-hidden="true">
      <polygon points="0,0 214,0 175,48 262,109 0,109" fill="url(#blue-glow)"/>
    </svg>
    <svg class="megaphone" aria-hidden="true"><use href="#icon-megaphone"/></svg>
    <div class="copy">
      <div class="tagline-top">A COMPLETE RANGE</div>
      <div class="tagline-main">OF SOFTWARE</div>
      <div class="brand"><span class="brand-square"></span>Novalith</div><br>
      <a class="cta">READ MORE</a>
    </div>
  </section>

  <!-- Leaderboard -->
  <div class="size-label" style="left:175px;top:968px">728_90</div>
  <section class="banner leaderboard">
    <div class="banner-art" style="right:0" role="img" aria-label="Grayscale illustration of hands typing on a laptop between hands holding a coin and a card"></div>
    <svg class="banner-shape" viewBox="0 0 870 108" preserveAspectRatio="none" aria-hidden="true">
      <polygon points="0,0 422,0 494,108 0,108" fill="url(#blue-glow)"/>
    </svg>
    <svg class="megaphone" aria-hidden="true"><use href="#icon-megaphone"/></svg>
    <div class="copy">
      <div class="tagline-main">A COMPLETE&nbsp; RANGE OF SOFTWARE</div>
      <div class="cta-row">
        <a class="cta">READ MORE</a>
        <div class="brand"><span class="brand-square"></span>Novalith</div>
      </div>
    </div>
  </section>

  <!-- Half page -->
  <div class="size-label" style="left:708px;top:66px">300_600</div>
  <section class="banner half-page">
    <div class="banner-art" role="img" aria-label="Grayscale illustration of hands typing on a laptop under a gear with a euro coin and bar charts"></div>
    <svg class="banner-shape" viewBox="0 0 327 654" preserveAspectRatio="none" aria-hidden="true">
      <polygon points="0,240 162,312 327,212 327,654 0,654" fill="url(#blue-glow)"/>
    </svg>
    <svg class="megaphone" aria-hidden="true"><use href="#icon-megaphone"/></svg>
    <div class="copy">
      <div class="brand"><span class="brand-square"></span>Novalith</div>
      <div class="tagline-top">A COMPLETE&nbsp; RANGE</div>
      <div class="tagline-main">OF SOFTWARE</div>
      <a class="cta">READ MORE</a>
    </div>
  </section>
</main>
</body>
</html>
```